Kip's Pharmacy Business Card Design Project

I need a business card designed for my pharmacy Kip's Pharmacy. I would like just the logo on one side, maybe with black background and white lettering. The other side I would also like to include my logo which is attached. Also, please include my name and the following information:
Rolf Mayhew Owner/Pharm D.
Business address is 7314 N Birchwood Rd Sioux Falls, SD 57193.
Phone number is 605-318-2067 and fax # is 605-318-2063.
my email address is kip@kipsrxhall.com.
My website is www.kipsrxhall.com.
My business hours are Monday-Friday 8am-7 pm. Saturday 8am-12 pm. Sunday Closed.
I would like the design to include my logo colors, black, white, and neon green. Silver may be added as a highlight. Thanks.
Industry/Entity Type
Pharmacy
Contact Information for Business Card
See above in product description
Look and feel

```html
<!DOCTYPE html>
<html lang="en">
<head>
<meta charset="utf-8">
<title>Kip's Pharmacy – Business Card</title>
<link rel="stylesheet" href="https://fonts.googleapis.com/css2?family=Open+Sans:wght@400;600;700&display=swap">
<style>
  :root {
    --stage: #2b2b2b;
    --neon-green: #7bc121;
    --card-white: #ffffff;
    --ink: #1d1d1d;
    --rule: #2a2a2a;
    --soft-shadow: rgba(0, 0, 0, 0.45);
  }
  * { box-sizing: border-box; margin: 0; padding: 0; }
  html, body {
    width: 1200px; height: 900px; overflow: hidden;
    background: var(--stage);
    font-family: "Open Sans", Arial, sans-serif;
  }
  .canvas { position: relative; width: 1200px; height: 900px; }

  .card {
    position: absolute; width: 700px; height: 400px;
    border-radius: 26px;
    box-shadow: 0 14px 34px var(--soft-shadow);
    overflow: hidden;
  }

  /* Front side */
  .card-front { left: 100px; top: 40px; background: var(--neon-green); }
  .front-brand {
    position: absolute; inset: 0;
    display: flex; align-items: center; justify-content: center; gap: 22px;
  }
  .front-brand .brand-dot {
    width: 34px; height: 34px; border-radius: 50%; background: var(--card-white);
  }
  .front-brand .brand-name {
    color: var(--card-white); font-weight: 600; font-size: 54px; letter-spacing: -0.5px;
  }

  /* Back side */
  .card-back { left: 400px; top: 470px; background: var(--card-white); color: var(--ink); }

  .back-header {
    position: absolute; right: 44px; top: 34px;
    display: flex; align-items: center; gap: 18px;
  }
  .back-header .brand-dot { width: 22px; height: 22px; border-radius: 50%; background: var(--neon-green); }
  .back-header .header-divider { width: 1.5px; height: 52px; background: var(--rule); }
  .back-header .brand-name { font-weight: 600; font-size: 30px; letter-spacing: -0.4px; }

  .address {
    position: absolute; left: 44px; top: 118px;
    font-size: 14px; line-height: 1.35; font-weight: 600;
  }

  .hours {
    position: absolute; right: 44px; top: 112px;
    font-size: 17px; line-height: 1.3;
  }
  .hours-title { color: var(--neon-green); text-transform: uppercase; font-size: 17px; }
  .hours-row { display: grid; grid-template-columns: 96px auto; }
  .hours-row .time::before { content: "| "; }

  .person {
    position: absolute; left: 44px; top: 222px; right: 44px;
  }
  .person-name { color: var(--neon-green); font-weight: 700; font-size: 18px; }
  .person-line { display: flex; align-items: flex-end; gap: 8px; }
  .person-title { font-size: 18px; white-space: nowrap; }
  .person-rule { flex: 1; height: 1.5px; background: var(--rule); margin-bottom: 8px; }

  .contacts {
    position: absolute; left: 44px; top: 290px;
    list-style: none; font-size: 18px; line-height: 24px;
  }
  .contacts li { display: flex; align-items: center; gap: 10px; }
  .contacts svg { width: 16px; height: 16px; fill: var(--neon-green); flex: none; }
</style>
</head>
<body>
<main class="canvas">

  <section class="card card-front" aria-label="Card front">
    <div class="front-brand">
      <span class="brand-dot"></span>
      <span class="brand-name">Kip's Pharmacy</span>
    </div>
  </section>

  <section class="card card-back" aria-label="Card back">
    <header class="back-header">
      <span class="brand-dot"></span>
      <span class="header-divider"></span>
      <span class="brand-name">Kip's Pharmacy</span>
    </header>

    <address class="address" style="font-style:normal">
      7314 N Birchwood Rd<br>Sioux Falls, SD 57193
    </address>

    <div class="hours">
      <div class="hours-title">Business Hours</div>
      <div class="hours-row"><span>Mon–Fr</span><span class="time">8am–7pm</span></div>
      <div class="hours-row"><span>Saturday</span><span class="time">8am–12pm</span></div>
      <div class="hours-row"><span>Sunday</span><span class="time">Closed</span></div>
    </div>

    <div class="person">
      <div class="person-name">Rolf Mayhew</div>
      <div class="person-line">
        <span class="person-title">Owner/Pharm D.</span>
        <span class="person-rule"></span>
      </div>
    </div>

    <ul class="contacts">
      <li>
        <svg viewBox="0 0 16 16" aria-label="Phone"><path d="M4 1l3 3-1.6 1.8a9 9 0 0 0 4.8 4.8L12 9l3 3-2 2.5C6.5 14 2 9.5 1.5 3z"/></svg>
        605-318-2067
      </li>
      <li>
        <svg viewBox="0 0 16 16" aria-label="Fax"><path d="M4 1h8v4H4zM1 6h14v6h-3v3H4v-3H1zM5 10v4h6v-4z"/></svg>
        605-318-2063
      </li>
      <li>
        <svg viewBox="0 0 16 16" aria-label="Email"><path d="M1 3h14v10H1zM2.5 4.5v.6L8 9l5.5-3.9v-.6z"/></svg>
        kip@kipsrxhall.com
      </li>
      <li>
        <svg viewBox="0 0 16 16" aria-label="Website"><path d="M8 1a7 7 0 1 0 0 14A7 7 0 0 0 8 1zm0 1.5c.9 1 1.5 2.6 1.7 4.5H6.3C6.5 5.1 7.1 3.5 8 2.5zM2.6 7h2.2c.1-1.7.5-3.2 1.2-4.2A5.5 5.5 0 0 0 2.6 7zm8.6 0h2.2A5.5 5.5 0 0 0 10 2.8c.7 1 1.1 2.5 1.2 4.2zM2.6 9a5.5 5.5 0 0 0 3.4 4.2c-.7-1-1.1-2.5-1.2-4.2zm3.7 0c.2 1.9.8 3.5 1.7 4.5.9-1 1.5-2.6 1.7-4.5zm4.9 0c-.1 1.7-.5 3.2-1.2 4.2A5.5 5.5 0 0 0 13.4 9z"/></svg>
        www.kipsrxhall.com
      </li>
    </ul>
  </section>

</main>
</body>
</html>
```